Packaging Tape Design for Retail / Ecommerce Company

We need a design for custom packing tape for our company. We would like to see two designs for the packaging tape. 1) with the word fragile attached 2) Similiar design without the fragileMinimum resolution is 300 .ppi 3" x 6" or 3" x 12" - If selected, request that font that are used be identified. Orla Hearth Logo and package - Nest Bright! is a tagline we use on documents and correspondence. Looking for a creative design.

Target Market(s)

Mid level to high end consumers

Industry/Entity Type

Retail

Font styles to use
Sans Serif

Requirements
Must have
• logo must be included
• Nest Bright! - must be included
• web address: orlahearth.com
Nice to have
• creativity

```html
<!DOCTYPE html>
<html lang="en">
<head>
<meta charset="utf-8">
<title>Orla Hearth Packing Tape</title>
<link rel="stylesheet" href="https://fonts.googleapis.com/css2?family=Oswald:wght@700&family=Source+Sans+3:wght@400;700&display=swap">
<style>
  :root {
    --backdrop: #ffffff;
    --tape: #dad8b2;
    --ink: #7a1e0c;
  }
  html, body {
    margin: 0;
    padding: 0;
    overflow: hidden;
  }
  .canvas {
    width: 1106px;
    height: 1200px;
    background: var(--backdrop);
    display: flex;
    flex-direction: column;
    justify-content: center;
    gap: 24px;
    overflow: hidden;
  }
  .tape-strip {
    height: 276px;
    background: var(--tape);
    display: flex;
    align-items: center;
    box-sizing: border-box;
    color: var(--ink);
  }
  .tape-strip--fragile {
    padding: 0 46px 0 52px;
    justify-content: space-between;
  }
  .tape-strip--plain {
    padding: 0 40px;
    justify-content: space-between;
  }
  .brand-name {
    font-family: "Oswald", sans-serif;
    font-weight: 700;
    color: var(--ink);
    letter-spacing: 1px;
    white-space: nowrap;
  }
  .tape-strip--fragile .brand-name { font-size: 42px; }
  .tape-strip--plain .brand-name { font-size: 33px; }
  .tagline-block {
    display: flex;
    flex-direction: column;
    align-items: flex-start;
  }
  .tagline {
    font-family: "Oswald", sans-serif;
    font-weight: 700;
    text-transform: uppercase;
    line-height: 1;
    white-space: nowrap;
  }
  .web-address {
    font-family: "Source Sans 3", sans-serif;
    font-weight: 400;
    white-space: nowrap;
    margin-top: 6px;
  }
  .tape-strip--fragile .tagline { font-size: 60px; }
  .tape-strip--fragile .web-address { font-size: 26px; }
  .tape-strip--plain .tagline { font-size: 46px; }
  .tape-strip--plain .web-address { font-size: 20px; }
  .fragile-box {
    border: 2px solid var(--ink);
    width: 316px;
    height: 114px;
    display: flex;
    align-items: center;
    justify-content: center;
    box-sizing: border-box;
    font-family: "Source Sans 3", sans-serif;
    font-weight: 700;
    font-size: 62px;
    letter-spacing: 1px;
  }
</style>
</head>
<body>
  <main class="canvas">
    <section class="tape-strip tape-strip--fragile" aria-label="Packing tape with fragile notice">
      <div class="brand-name">ORLA HEARTH</div>
      <div class="tagline-block">
        <div class="tagline">Nest Bright!</div>
        <div class="web-address">http://orlahearth.com/</div>
      </div>
      <div class="fragile-box">FRAGILE</div>
    </section>

    <section class="tape-strip tape-strip--plain" aria-label="Packing tape without fragile notice">
      <div class="brand-name">ORLA HEARTH</div>
      <div class="tagline-block">
        <div class="tagline">Nest Bright!</div>
        <div class="web-address">http://orlahearth.com/</div>
      </div>
      <div class="brand-name">ORLA HEARTH</div>
      <div class="tagline-block">
        <div class="tagline">Nest Bright!</div>
        <div class="web-address">http://orlahearth.com/</div>
      </div>
    </section>
  </main>
</body>
</html>
```